REALTOR/REALESTATE INVESTOR CARD

I AM MY LOCAL CITIES FLIP THIS HOUSE KING...I CHANGE NEIGHBORHOODS ONE HOUSE AT A TIME. I BUY OLD HOUSES FOR CASH TOTALLY RENOVATE THEM TO LIKE NEW, THEN RE SELL THEM...
I HAVE BEEN USING PLATINUM & BURGANDY AS MY MAIN COLOR..
I WANT SOMETHING FUN AND MODERN TO APPEAL TO ALL BUYERS AND SELLERS. AND TO REFLECT I AM AT THE TOP OF MY GAME...A WOW...THIS IS A GREAT CARD.......WOW.......I AM A REALTOR....I FLIP HOUSES.....MAYBE SHOW AND OLD HOUSE AND THEN A SPARKLING NEW HOUSE..... MY COMPANY NAME IS HARBORLINE PROPERTY PARTNERS THE ADDRESS IS P.O.BOX 738 GOOSE CREEK, S.C. 29445

Target Market(s)

I SELL HOUSES THAT HAVE BEEN RENOVATED TO ALMOST BRAND NEW CONDITION.......I ALSO BUY HOUSES/MOBILES FOR ALL CASH FAST CLOSINGS..
I BUY GOOSE CREEK HOUSES ALL CASH FAST CLOSE.....I BUY MOBILE HOMES ANY CONDITION, ANY PRICE.....Buyers & sellers of houses.....

Industry/Entity Type

Investment

Font styles to use
Sans Serif

Requirements
Must have
• I BUY GOOSE CREEK HOUSES ALL CASH FAST CLOSINGS......
CHANGING GOOSE CREEK, ONE HOUSE AT A TIME...
RAY T. ELLWOOD CIAS
REALTOR/CERTIFIED INVESTOR AGENT
HARBORLINE PROPERTY PARTNERS,LLC.
P.O. BOX 738
GOOSE CREEK, S.C. 29445
843-555-0172
RAYELLWOODHOUSES@QUILLMAIL.EXAMPLE
Nice to have
• GOOSE CREEK'S RE-HAB KING....
A actual picture of MAYBE A HOME BEING RENOVATED
TO ONE LOOKING AWESOME.....artwork
Should not have
• a picture of and old ugly home the a sparkling brand new one that is what I di I renovate homes.......

```html
<!DOCTYPE html>
<html lang="en">
<head>
<meta charset="utf-8">
<title>Harborline Property Partners – Business Card</title>
<link rel="stylesheet" href="https://fonts.googleapis.com/css2?family=Tinos:wght@400;700&display=swap">
<style>
  :root {
    --backdrop: #1e1f20;
    --card-slate: #5a5d5d;
    --card-paper: #f3f3f1;
    --band-slate: #6a6d6d;
    --ink-light: #f4f4f4;
    --ink-grey: #5e6061;
  }
  html, body {
    margin: 0;
    width: 1200px;
    height: 1024px;
    overflow: hidden;
    background: var(--backdrop);
  }
  .canvas {
    position: relative;
    width: 1200px;
    height: 1024px;
    font-family: "Tinos", "Times New Roman", serif;
  }
  .card {
    position: absolute;
    left: 220px;
    width: 760px;
    height: 440px;
    border-radius: 22px;
    overflow: hidden;
    box-sizing: border-box;
    display: flex;
    flex-direction: column;
    align-items: center;
    justify-content: center;
    text-align: center;
  }
  .card-back {
    top: 48px;
    background: var(--card-slate);
  }
  .slogan {
    margin: 0;
    color: var(--ink-light);
    font-size: 21px;
    line-height: 1.45;
    letter-spacing: 0.5px;
    text-transform: uppercase;
    padding-left: 40px;
  }
  .card-front {
    top: 536px;
    background: var(--card-paper);
    padding-bottom: 34px;
  }
  .edge-band {
    position: absolute;
    left: 0;
    right: 0;
    bottom: 0;
    height: 34px;
    background: var(--band-slate);
    border-top: 4px solid #d9d9d7;
  }
  .card-front .title {
    margin: 0 0 22px;
    color: var(--ink-grey);
    font-weight: 700;
    font-size: 27px;
    line-height: 1.15;
    letter-spacing: 0.6px;
    text-shadow: 0 1px 0 #ffffff;
  }
  .pitch, .contact {
    margin: 0;
    color: var(--ink-grey);
    font-size: 17px;
    line-height: 1.3;
    letter-spacing: 0.4px;
    text-shadow: 0 1px 0 #ffffff;
  }
  .pitch { margin-bottom: 24px; }
  .contact .email { text-transform: lowercase; display: block; margin-bottom: 10px; }
</style>
</head>
<body>
<main class="canvas">
  <section class="card card-back">
    <p class="slogan">
      Goose Creek's Re-Hab King....<br>
      Maybe a home being renovated<br>
      to one looking awesome.....
    </p>
  </section>

  <section class="card card-front">
    <h1 class="title">
      REALTOR/CERTIFIED INVESTOR AGENT<br>
      HARBORLINE PROPERTY PARTNERS,LLC
    </h1>
    <p class="pitch">
      I BUY GOOSE CREEK HOUSES ALL CASH FAST CLOSINGS.....<br>
      CHANGING GOOSE CREEK, ONE HOUSE AT A TIME...<br>
      RAY T. ELLWOOD CIAS
    </p>
    <p class="contact">
      <span class="email">rayellwoodhouses@quillmail.example</span>
      P.O. BOX 738, GOOSE CREEK, S.C. 29445, 843-555-0172
    </p>
    <div class="edge-band"></div>
  </section>
</main>
</body>
</html>
```